An original design for a not-so-original website

We're looking to launch a Tessarel offer on a foreign market soon.

The company is called QMR Solutions (Solutions is not necessary). We have no logo or color code or anything else.

Our website will have a content very similar to:
http://vestrunio.net/
The idea is to use the content of this website for your designs, with the following differences:
- home page will have the Tessarel offer instead of Morvex:
http://vestrunio.net/secure-online-storage-tessarel
- there will not be an event page
- ours will be French/English (flags/links)

About the design itself, we have no idea at all - that's why we're here.

The design should be PSD file, no coding required!

For any question, please feel free to contact me

UPDATE: I don't want photos in the design, partticulary no people, hands, laptops, mobiles, visit cards. The homepage should be the one about Tessarel. That's the one that matters. Please don't use Lorem Ipsum text, copy and paste the text from the link I've given, that will give a better idea. No map either (or small on the contact page but for now let's just focus on the home)
Updates

Hi everyone,

I am deeply ssorry I haven't been able to give any feedback. I'm in the middle of nowhere for a few days and don't have Internet access - except right now!

I'll be back very soon.

Don't spend too much time on the logo, I think I will post a specific project once I have the website.

Thanks for all the designs!

Sorry the very short reviews, and more sorry to the ones I couldn't review yet. I'll try to do it tomorrow.

Thanks!

Target Market(s)

Professionals

Industry/Entity Type

It Company

Font styles to use
Serif
Sans Serif

Requirements
Should not have
• Photos, Lorem Ipsum text

```html
<!DOCTYPE html>
<html lang="en">
<head>
<meta charset="utf-8">
<title>QMR Solutions — Tessarel</title>
<link href="https://fonts.googleapis.com/css2?family=Open+Sans:wght@400;600;700&family=Roboto:wght@400;500&display=swap" rel="stylesheet">
<style>
:root{
  --blue:#1d9fca;
  --blue-dark:#0f77a0;
  --ink:#333;
  --muted:#777;
  --topbar:#3b3b3b;
  --footer-deep:#2f2f2f;
  --band:#3a3a3a;
  --soft:#f4f4f4;
  --line:#e2e2e2;
  --white:#fff;
}
*{box-sizing:border-box;margin:0;padding:0}
html,body{width:807px;height:1200px;overflow:hidden;background:var(--white)}
body{font-family:"Roboto",Arial,sans-serif;color:var(--ink);position:relative}
.wrap{position:absolute;left:107px;width:592px}
a{color:inherit;text-decoration:none}

.topbar{position:absolute;top:0;left:0;width:807px;height:20px;background:var(--topbar)}
.topbar .wrap{top:0;height:20px;display:flex;align-items:center;justify-content:space-between;font-size:7px;color:#9a9a9a;letter-spacing:.3px}
.topbar nav a{margin-right:10px}
.topbar nav a.current{color:#ddd}
.lang{display:flex;align-items:center;gap:6px}
.lang svg{display:block}

.header{position:absolute;top:20px;left:0;width:807px;height:64px;background:linear-gradient(#fff,#f3f3f3)}
.brand{position:absolute;left:107px;top:20px;font-family:"Open Sans",sans-serif;font-size:25px;font-weight:400;color:var(--blue);letter-spacing:-.5px;line-height:1}
.brand-tag{position:absolute;left:204px;top:46px;font-size:5.5px;color:#555;letter-spacing:.3px}
.mainnav{position:absolute;top:25px;left:299px;display:flex;font-size:8.5px;color:#444}
.mainnav a{padding:4px 10px;border-radius:10px;margin-right:2px}
.mainnav a.active{background:var(--blue);color:#fff}

.hero{position:absolute;top:84px;left:0;width:807px;height:293px;background:linear-gradient(135deg,#22a8d4,#1896c0 60%,#1d9fca);overflow:hidden}
.hero h1{position:absolute;top:18px;width:807px;text-align:center;font-family:"Open Sans",sans-serif;font-weight:400;font-size:23px;line-height:30px;color:#fff}
.hero h1 b{font-weight:700}
.hero p{position:absolute;top:82px;left:227px;width:360px;font-family:"Open Sans",sans-serif;font-size:12.5px;line-height:15px;color:var(--blue-dark)}
.hero-deco{position:absolute;top:128px;left:230px;width:350px;height:130px;background:radial-gradient(ellipse at center,rgba(15,110,146,.25),rgba(15,110,146,0) 70%)}
.quote-art{position:absolute;top:169px;left:291px;width:245px;height:124px;border-radius:60px 60px 0 0;background:radial-gradient(ellipse at 50% 70%,#ffffff 55%,#e9f5fa 100%)}

.offer{position:absolute;top:377px;left:107px;width:592px;height:41px;background:var(--band);border-radius:0 0 5px 5px;box-shadow:0 3px 0 #222}
.offer h2{position:absolute;left:23px;top:7px;font-family:"Open Sans",sans-serif;font-weight:400;font-size:22px;color:#fff;letter-spacing:-.2px}
.btn{display:inline-block;border-radius:11px;font-size:8.5px;color:#fff;text-align:center}
.btn-blue{background:var(--blue);box-shadow:inset 0 -2px 0 rgba(0,0,0,.15)}
.btn-dark{background:#3c3c3c}
.offer .btn{position:absolute;right:11px;top:12px;width:66px;height:17px;line-height:17px}

.intro{position:absolute;top:418px;left:0;width:807px;height:378px;background:var(--soft)}
.intro h2{position:absolute;top:70px;width:807px;text-align:center;font-family:"Open Sans",sans-serif;font-weight:400;font-size:16.5px;line-height:23px;color:#333}
.intro h2 b{font-weight:700}
.intro h2 .hl{color:var(--blue);font-weight:700}
.intro .lead{position:absolute;top:126px;left:150px;width:507px;text-align:center;font-size:7.8px;line-height:12px;color:#666}
.services{position:absolute;top:222px;left:107px;width:592px;display:flex;justify-content:space-between}
.service{width:188px;text-align:center}
.service .icon{width:40px;height:38px;margin:0 auto 10px;background:linear-gradient(#3a3a3a,#2a2a2a);border-radius:18px 18px 4px 4px}
.service .icon.accent{background:linear-gradient(#4ab6dd,#1d9fca);border-radius:4px}
.service h3{font-family:"Open Sans",sans-serif;font-weight:400;font-size:10.5px;color:#333;margin-bottom:7px}
.service h3.hl{color:var(--blue)}
.service p{font-size:7.5px;line-height:12px;color:#777}
.service p a{color:#333;font-style:italic;text-decoration:underline}
.service p a.hl{color:var(--blue)}

.plans{position:absolute;top:823px;left:107px;width:592px;display:flex;justify-content:space-between}
.plan{width:182px;height:157px;background:#f7f7f7;border:1px solid var(--line)}
.plan h4{height:22px;line-height:22px;padding-left:9px;background:var(--blue);font-family:"Open Sans",sans-serif;font-weight:400;font-size:10px;color:#fff;width:181px}
.plan ul{list-style:none;padding:4px 0 0}
.plan li{display:flex;align-items:center;height:17.5px;padding-left:6px;font-size:7.4px;color:#888;border-bottom:1px solid #efefef}
.plan li::before{content:"";width:7px;height:7px;border-radius:50%;border:1px solid #e2e2e2;background:#fafafa;margin-right:6px}
.plan li.on{color:#333}
.plan li.on::before{border:2px solid #cfe9f3;background:var(--blue)}
.plan .btn{display:block;margin:6px auto 0;width:67px;height:17px;line-height:17px}

.footer{position:absolute;top:1009px;left:0;width:807px;height:171px;background:linear-gradient(135deg,#444,#383838 50%,#424242);border-top:2px solid #2a2a2a}
.fcol{position:absolute;width:170px;color:#bbb}
.fcol h5{font-family:"Roboto",sans-serif;font-weight:400;font-size:12px;color:#fff;margin-bottom:6px}
.fcol p,.fcol li{font-size:6.8px;line-height:11px;list-style:none}
.fcol li.current{text-decoration:underline}
.rule{position:absolute;top:110px;height:1px;width:160px;background:#505050}
.social{display:flex;gap:8px}
.social span{width:20px;height:20px;background:#777;display:block}
.social span.first{background:var(--blue)}
.field{display:flex;align-items:center;width:158px;height:18px;background:#8a8a8a;border:1px solid #999;font-size:6.5px;color:#eee;padding-left:6px}
.field.dark{background:#3a3a3a;border-color:#5a5a5a;color:#888;justify-content:space-between;padding-right:6px}
.copy{position:absolute;top:1180px;left:0;width:807px;height:20px;background:var(--footer-deep);color:#aaa;font-size:7.5px;text-align:center;line-height:20px}
</style>
</head>
<body>

<header class="topbar">
  <div class="wrap">
    <nav><a href="#">HELP</a><a href="#">FAQ</a><a href="#" class="current">SUPPORT</a><a href="#">PRIVACY POLICY</a></nav>
    <div class="lang">LANGUAGE
      <svg width="17" height="10" viewBox="0 0 17 10" role="img" aria-label="English">
        <rect width="17" height="10" fill="#fff"/><rect width="17" height="1.5" fill="#c33"/><rect y="3" width="17" height="1.5" fill="#c33"/><rect y="6" width="17" height="1.5" fill="#c33"/><rect y="8.5" width="17" height="1.5" fill="#c33"/><rect width="7" height="5.5" fill="#2a4a8f"/>
      </svg>
      <svg width="15" height="10" viewBox="0 0 15 10" role="img" aria-label="Français">
        <rect width="5" height="10" fill="#2a4a8f"/><rect x="5" width="5" height="10" fill="#fff"/><rect x="10" width="5" height="10" fill="#c33"/>
      </svg>
    </div>
  </div>
</header>

<div class="header">
  <div class="brand">QMR Solutions</div>
  <div class="brand-tag">TESSAREL OFFER</div>
  <nav class="mainnav">
    <a href="#" class="active">Home</a><a href="#">What We Do</a><a href="#">How We Work</a><a href="#">What we use</a><a href="#">Contact Us</a>
  </nav>
</div>

<section class="hero">
  <h1>WE SPECIALISE IN <b>ENTERPRISE</b> LINUX<br>AND <b>OPEN SOURCE</b> SOLUTIONS</h1>
  <p>At Vestrunio, we design, implement, maintain and support IT infrastructure based on Linux and open source software.</p>
  <div class="hero-deco" role="img" aria-label="Faint IT icons scattered around the quote artwork"></div>
  <div class="quote-art" role="img" aria-label="White cloud artwork with Request a Free Quote lettering"></div>
</section>

<div class="offer">
  <h2>WE OFFER TESSAREL IN THREE FLAVOURS!</h2>
  <a href="#" class="btn btn-blue">Read More</a>
</div>

<section class="intro">
  <h2>WE SPECIALISE IN <b>ENTERPRISE LINUX</b><br>AND <span class="hl">OPEN SOURCE</span> SOLUTIONS</h2>
  <p class="lead">At Vestrunio, we design, implement, maintain and support IT infrastructure based on Linux and open source software. With our consulting, organisations lower their IT capital costs and operational expenses. Our certified engineers help you reduce over-provisioning, consolidate servers and increase business agility and continuity.</p>
  <div class="services">
    <div class="service">
      <div class="icon" role="img" aria-label="Consulting icon"></div>
      <h3>CONSULTING</h3>
      <p>You want to get the most out of your investment. You want infrastructure and software that works and that keeps working. <a href="#">read more</a></p>
    </div>
    <div class="service">
      <div class="icon accent" role="img" aria-label="Support icon"></div>
      <h3 class="hl">SUPPORT AS YOU NEED IT</h3>
      <p>You want to get the most out of your investment. You want infrastructure and software that works and that keeps working. <a href="#" class="hl">read more</a></p>
    </div>
    <div class="service">
      <div class="icon" role="img" aria-label="Training icon"></div>
      <h3>TRAINING AND COACHING</h3>
      <p>You want to get the most out of your investment. You want infrastructure and software that works and that keeps working. <a href="#">read more</a></p>
    </div>
  </div>
</section>

<section class="plans">
  <div class="plan">
    <h4>ON PREMISES INSTALLATION</h4>
    <ul><li>You are in full control</li><li>Seamless integration with your infrastructure</li><li>LDAP integration</li><li class="on">Extendable through a powerful API</li><li>Optional 24/7 support contract</li><li>You are in full control</li></ul>
    <a href="#" class="btn btn-blue">Read More</a>
  </div>
  <div class="plan">
    <h4>ON PREMISES INSTALLATION</h4>
    <ul><li>You are in full control</li><li>Seamless integration with your infrastructure</li><li>LDAP integration</li><li>Extendable through a powerful API</li><li>Optional 24/7 support contract</li><li>You are in full control</li></ul>
    <a href="#" class="btn btn-dark">Read More</a>
  </div>
  <div class="plan">
    <h4>ON PREMISES INSTALLATION</h4>
    <ul><li>You are in full control</li><li>Seamless integration with your infrastructure</li><li>LDAP integration</li><li>Extendable through a powerful API</li><li>Optional 24/7 support contract</li><li>You are in full control</li></ul>
    <a href="#" class="btn btn-dark">Read More</a>
  </div>
</section>

<footer class="footer">
  <div class="fcol" style="left:108px;top:12px">
    <h5>QMR Solutions</h5>
    <p>At Vestrunio, we design, implement, maintain and support IT infrastructure based on Linux and open source software. With our consulting, organisations lower their IT capital costs and operational expenses.</p>
  </div>
  <div class="fcol" style="left:315px;top:12px">
    <h5>Quick Links</h5>
    <ul><li class="current">Home</li><li>What We Do</li><li>How We Work</li><li>What We Us</li><li>Contact Us</li></ul>
  </div>
  <div class="fcol" style="left:520px;top:12px">
    <h5>Products &amp; Services</h5>
    <ul><li class="current">On Premises Installation</li><li>Suport Us You Need It</li><li>Trainning and Coaching</li><li>Consulting</li><li>per user on our platform</li><li>on a Virtual Machine in the cloud</li></ul>
  </div>
  <div class="rule" style="left:108px"></div><div class="rule" style="left:315px"></div><div class="rule" style="left:520px"></div>
  <div class="fcol" style="left:108px;top:122px">
    <h5>Connect!</h5>
    <div class="social"><span class="first"></span><span></span><span></span><span></span><span></span></div>
  </div>
  <div class="fcol" style="left:314px;top:122px">
    <h5>Search Here</h5>
    <div class="field">Enter your search keyword</div>
  </div>
  <div class="fcol" style="left:520px;top:122px">
    <h5>Subscribe a Newsletter</h5>
    <div class="field dark">Enter Your Email Address
      <svg width="16" height="10" viewBox="0 0 16 10"><rect x=".5" y=".5" width="15" height="9" fill="none" stroke="#888"/><path d="M.5 .5 L8 6 L15.5 .5" fill="none" stroke="#888"/></svg>
    </div>
  </div>
</footer>
<div class="copy">Copyright © 2013 QMR Solutions</div>

</body>
</html>
```